Life Coaching business needs a new flyer

We are an Australian business that specialises in Life Coaching, Career Coaching, Health and Wellness Coaching, Yoga and Pilates. We need a A4 double sided flyer that is full colour and folded to DL format. I have attached a couple of designs that I like and some pictures and would like the flyer to be bright yet stylish.

Life Coaching

```html
<!DOCTYPE html>
<html lang="en">
<head>
<meta charset="utf-8">
<title>Bright Path Coaching – Trifold Flyer</title>
<link rel="stylesheet" href="https://fonts.googleapis.com/css2?family=Open+Sans:wght@400;600;700&family=Montserrat:wght@500;600&display=swap">
<style>
  :root {
    --brand-blue: #1f7fc4;
    --deep-blue: #1b5f9e;
    --leaf-green: #6cbf3d;
    --text-grey: #666a6e;
    --paper: #ffffff;
    --mark: #b5b5b5;
  }
  * { margin: 0; padding: 0; box-sizing: border-box; }
  html, body { width: 1200px; height: 901px; overflow: hidden; background: var(--paper); }
  .canvas { position: relative; width: 1200px; height: 901px; overflow: hidden; font-family: "Open Sans", Arial, sans-serif; }
  .artwork { position: absolute; inset: 0; }

  .testimonials { position: absolute; left: 112px; top: 114px; width: 304px; color: var(--text-grey); font-size: 11.2px; line-height: 1.42; }
  .testimonials h2 { font-weight: 700; color: var(--deep-blue); font-size: 14.5px; margin-bottom: 2px; }
  .quote { text-align: justify; margin-bottom: 15px; }
  .quote cite { display: block; font-style: normal; text-align: left; }

  .brand { position: absolute; text-align: center; color: var(--deep-blue); font-family: "Montserrat", Arial, sans-serif; font-weight: 600; }
  .brand .dot { display: block; margin: 0 auto 10px; border-radius: 50%; background: var(--leaf-green); }
  .brand-center { left: 450px; top: 208px; width: 300px; font-size: 17px; }
  .brand-center .dot { width: 50px; height: 50px; }
  .brand-right { left: 790px; top: 100px; width: 330px; font-size: 21px; }
  .brand-right .dot { width: 78px; height: 78px; margin-bottom: 14px; }

  .intro { position: absolute; left: 445px; top: 322px; width: 310px; text-align: center; font-size: 11.2px; line-height: 15px; color: var(--text-grey); }
  .intro p + p { margin-top: 8px; }

  .offer { position: absolute; left: 459px; top: 449px; width: 270px; height: 63px; border: 2px solid var(--brand-blue); border-radius: 8px; background: var(--paper); text-align: center; font-weight: 700; font-size: 11.6px; line-height: 1.35; color: #444; padding-top: 6px; }

  .contact { position: absolute; left: 430px; top: 713px; width: 340px; text-align: center; }
  .services-small { font-family: "Montserrat", Arial, sans-serif; font-weight: 600; font-size: 9px; color: var(--deep-blue); }
  .phone { font-family: "Montserrat", Arial, sans-serif; font-weight: 600; font-size: 14.5px; color: var(--deep-blue); margin-top: 3px; display: flex; justify-content: center; align-items: center; gap: 5px; }
  .email, .web { font-family: "Montserrat", Arial, sans-serif; font-weight: 500; font-size: 11.5px; color: #555; margin-top: 4px; }

  .services-large { position: absolute; left: 775px; top: 734px; width: 356px; text-align: center; font-family: "Montserrat", Arial, sans-serif; font-weight: 500; font-size: 16.5px; color: var(--deep-blue); }
  .web-large { position: absolute; left: 775px; top: 766px; width: 356px; text-align: center; font-family: "Montserrat", Arial, sans-serif; font-weight: 600; font-size: 12px; color: #666; }
</style>
</head>
<body>
<div class="canvas">
  <svg class="artwork" viewBox="0 0 1200 901" width="1200" height="901">
    <defs>
      <linearGradient id="leftPanelGrad" x1="0" y1="0" x2="1" y2="0">
        <stop offset="0" stop-color="#dcebf8"/><stop offset="1" stop-color="#f7fbfe"/>
      </linearGradient>
      <linearGradient id="midPanelGrad" x1="0" y1="0" x2="0" y2="1">
        <stop offset="0" stop-color="#ffffff"/><stop offset="0.3" stop-color="#f1f2f3"/><stop offset="0.7" stop-color="#eef1f3"/><stop offset="1" stop-color="#cfe6f7"/>
      </linearGradient>
      <linearGradient id="sunsetGrad" x1="0" y1="0" x2="1" y2="1">
        <stop offset="0" stop-color="#f6d59a"/><stop offset="0.45" stop-color="#c98a5c"/><stop offset="1" stop-color="#4e6678"/>
      </linearGradient>
      <linearGradient id="skyGrad" x1="0" y1="0" x2="0" y2="1">
        <stop offset="0" stop-color="#8fc8ec"/><stop offset="0.55" stop-color="#bfe0f2"/><stop offset="0.75" stop-color="#e57fb2"/><stop offset="1" stop-color="#d85f9a"/>
      </linearGradient>
      <linearGradient id="portraitGrad" x1="0" y1="0" x2="1" y2="1">
        <stop offset="0" stop-color="#c9b8a6"/><stop offset="1" stop-color="#4a3b33"/>
      </linearGradient>
    </defs>

    <g stroke="var(--mark)" stroke-width="1">
      <line x1="0" y1="68" x2="50" y2="68"/><line x1="68" y1="0" x2="68" y2="50"/>
      <line x1="1150" y1="68" x2="1200" y2="68"/><line x1="1131" y1="0" x2="1131" y2="50"/>
      <line x1="0" y1="828" x2="50" y2="828"/><line x1="68" y1="850" x2="68" y2="901"/>
      <line x1="1150" y1="828" x2="1200" y2="828"/><line x1="1131" y1="850" x2="1131" y2="901"/>
      <line x1="425" y1="0" x2="425" y2="50"/><line x1="775" y1="0" x2="775" y2="50"/>
      <line x1="425" y1="850" x2="425" y2="901"/><line x1="775" y1="850" x2="775" y2="901"/>
    </g>

    <rect class="panel-left" x="68" y="68" width="357" height="760" fill="url(#leftPanelGrad)"/>
    <rect class="panel-middle" x="425" y="68" width="350" height="760" fill="url(#midPanelGrad)"/>
    <rect class="panel-right" x="775" y="68" width="356" height="760" fill="var(--paper)"/>

    <path class="photo-hero" role="img" aria-label="Photo of a joyful young woman with raised arms beside a pink convertible under a blue sky"
      d="M775,225 C900,250 1040,285 1131,270 L1131,630 C1040,660 900,690 775,660 Z" fill="url(#skyGrad)"/>

    <path d="M425,205 C560,165 700,180 800,222 C920,272 1050,290 1131,262 L1131,68 L775,68 L775,180 C700,150 560,140 425,172 Z" fill="var(--paper)"/>
    <path d="M425,190 C560,150 700,165 800,210 C920,262 1050,278 1131,252" fill="none" stroke="var(--brand-blue)" stroke-width="9"/>
    <path d="M870,258 C960,288 1060,292 1131,268" fill="none" stroke="var(--leaf-green)" stroke-width="4"/>

    <path class="photo-group" role="img" aria-label="Photo of a group of smiling friends celebrating on a coastal road at sunset"
      d="M68,608 C190,580 320,578 425,605 L425,828 L68,828 Z" fill="url(#sunsetGrad)"/>
    <path d="M68,598 C180,560 320,558 425,590 L425,606 C320,580 190,584 68,612 Z" fill="var(--leaf-green)"/>

    <path d="M68,614 C200,580 330,578 440,612 C560,650 680,700 775,680 C900,655 1020,640 1131,612"
      fill="none" stroke="var(--brand-blue)" stroke-width="4"/>
    <path d="M775,680 C900,660 1020,640 1131,612 L1131,828 L775,828 Z" fill="var(--paper)"/>
    <path d="M775,676 C900,654 1020,630 1131,604" fill="none" stroke="var(--brand-blue)" stroke-width="7"/>
    <path d="M900,648 C980,632 1060,612 1131,590" fill="none" stroke="var(--leaf-green)" stroke-width="7"/>

    <circle cx="596" cy="610" r="86" fill="var(--brand-blue)"/>
    <circle cx="596" cy="610" r="81" fill="var(--paper)"/>
    <circle class="photo-portrait" role="img" aria-label="Portrait photo of the two coaches"
      cx="596" cy="610" r="78" fill="url(#portraitGrad)"/>
  </svg>

  <section class="testimonials">
    <h2>OUR HAPPY CLIENTS</h2>
    <div class="quote">“I have lost 10 kilos and now have the energy to play with my kids. Thanks Jenna for your support/guidance and helping me get rid of my limiting beliefs. I feel I can achieve anything now! The sky’s the limit”<cite>Megan, Mosman</cite></div>
    <div class="quote">“I had always wanted to start up own café however every time it came to putting it into practice I would procrastinate and not achieve anything. I became overwhelmed with the whole process and never achieved anything. Jenna put it into bite sized chunks and helped me to set small achievable goals. I am now a happy café owner.”<cite>Priya, Double Bay</cite></div>
    <div class="quote">“Jenna has helped to change my life around in all aspects. I would have been lost without her. Thanks Jenna for your professionalism, support and guidance.”<cite>Chloe, Cremorne</cite></div>
    <div class="quote">“I was so busy with kids, work, and my husband I lost who I was. Jenna has helped me find the person I am again.”<cite>Hannah, Chatswood</cite></div>
  </section>

  <div class="brand brand-center"><span class="dot"></span>Bright Path Coaching</div>

  <div class="intro">
    <p>Bright Path Coaching &amp; Meditation Centre<br>is a professional service that can<br>help you achieve the goals that you are looking for in<br>Life Coaching, Meditation, and Yoga/Pilates</p>
    <p>If you are ready to take your life<br>to the next level and would like to know more,<br>please contact us</p>
  </div>

  <div class="offer">Free Introductory Life Coaching<br>Phone/Video session -20 mins<br>(To see if coaching is right for you)</div>

  <div class="contact">
    <div class="services-small">LIFE COACHING • MEDITATION • YOGA/PILATES</div>
    <div class="phone">
      <svg width="15" height="15" viewBox="0 0 24 24" aria-hidden="true"><circle cx="12" cy="12" r="10.5" fill="none" stroke="currentColor" stroke-width="2"/><path d="M8.5 6.5l2 2-1.2 1.6c.7 1.6 2 2.9 3.6 3.6l1.6-1.2 2 2-1.3 1.8c-3.8-.4-7.8-4.4-8.2-8.2z" fill="currentColor"/></svg>
      02 9000 4172
    </div>
    <div class="email">hello@brightpathcoaching.com.au</div>
    <div class="web">www.brightpathcoaching.com.au</div>
  </div>

  <div class="brand brand-right"><span class="dot"></span>Bright Path Coaching</div>

  <div class="services-large">Life Coaching • Meditation • Yoga/Pilates</div>
  <div class="web-large">www.brightpathcoaching.com.au</div>
</div>
</body>
</html>
```